Velvet Bloom Marisol's Cleaning Service Business Cards Project

A business card with all contact details with logo design on there (already have a logo) eye catching Logo and contact info on one side, full logo on the back, must target upper class residential and corporate companies, fitness companies, still keep it on the feminine side of things , must look elegant

Target Market(s)

Upper class homes and corporate companies

Industry/Entity Type

Cleaning Service

Contact Information for Business Card

Name: Marisol Denhart
Position: Director
ABN: 47193062857
Email: marisolsvelvetcleaning@brightmail.example
Number: 0418926547

Font styles to use
Decorative

Colors

Designer to choose colors to be used in the design.

Requirements
Must have
• Available Sydney Wide, contact info and logo on one side, full logo on the back
Nice to have
• Professional appearance
Should not have
• Cheap advert looking stuff

```html
<!DOCTYPE html>
<html lang="en">
<head>
<meta charset="utf-8">
<title>Velvet Bloom – Business Cards</title>
<link rel="stylesheet" href="https://fonts.googleapis.com/css2?family=Cinzel:wght@500;600&family=Roboto:wght@400;500&display=swap">
<style>
  :root {
    --backdrop: #c4c4c4;
    --card-dark: #2e323f;
    --card-dark-tint: #333847;
    --teal: #32e6dc;
    --teal-soft: rgba(50, 230, 220, 0.22);
    --white: #ffffff;
    --white-soft: rgba(255, 255, 255, 0.28);
  }
  * { margin: 0; padding: 0; box-sizing: border-box; }
  html, body {
    width: 1200px; height: 960px; overflow: hidden;
    background: var(--backdrop);
    font-family: "Roboto", Arial, sans-serif;
  }
  .stage { position: relative; width: 1200px; height: 960px; }

  .card { position: absolute; width: 600px; height: 343px; overflow: hidden; }
  .card--front { left: 322px; top: 108px; background: var(--card-dark); }
  .card--back  { left: 320px; top: 493px; background: var(--teal); }

  /* brand wordmark */
  .brand { position: absolute; text-align: center; }
  .brand__name {
    display: block; font-family: "Cinzel", Georgia, serif;
    font-weight: 600; font-size: 20px; letter-spacing: 1px; line-height: 1;
  }
  .brand__tagline {
    display: block; font-family: "Roboto", Arial, sans-serif; font-weight: 500;
    font-size: 7.5px; letter-spacing: 2.2px; margin-top: 6px; white-space: nowrap;
  }
  .card--front .brand { left: 26px; top: 139px; width: 200px; color: var(--teal); }
  .card--front .brand__tagline { color: var(--white); }
  .card--back .brand { left: 140px; top: 118px; width: 320px; color: var(--white); }
  .card--back .brand__name { font-size: 30px; letter-spacing: 2px; }
  .card--back .brand__tagline { font-size: 10px; letter-spacing: 3px; margin-top: 8px; }

  .brand-dot { position: absolute; border-radius: 50%; }
  .card--front .brand-dot { left: 118px; top: 44px; width: 16px; height: 16px; background: var(--teal); }
  .card--back .brand-dot { left: 290px; top: 84px; width: 20px; height: 20px; background: var(--white); }

  /* ornament placeholders */
  .ornament { position: absolute; border-radius: 40px; }
  .card--front .ornament--crest { left: 30px; top: 94px; width: 190px; height: 34px; background: var(--teal-soft); }
  .card--back .ornament--crest { left: 145px; top: 186px; width: 300px; height: 60px; background: var(--white-soft); }
  .ornament--faint-swirl { left: 295px; top: 212px; width: 300px; height: 120px; background: var(--card-dark-tint); border-radius: 60px 0 0 60px; }
  .ornament--faint-symbol { left: 493px; top: 0; width: 107px; height: 200px; background: var(--card-dark-tint); border-radius: 50px 0 0 50px; }

  /* edge markers */
  .marker { position: absolute; left: 0; width: 11px; height: 14px; background: var(--teal); }
  .marker--one { top: 194px; }
  .marker--two { top: 212px; }

  .person { position: absolute; left: 30px; top: 190px; }
  .person__name { font-size: 21px; font-weight: 500; color: var(--teal); line-height: 1.1; letter-spacing: -0.2px; }
  .person__role { font-size: 15px; font-weight: 500; color: var(--teal); margin-top: 4px; }

  .details { position: absolute; left: 31px; top: 243px; color: var(--white); font-size: 14px; list-style: none; }
  .details__abn { margin-bottom: 6px; }
  .details li { display: flex; align-items: center; height: 19.5px; white-space: nowrap; }
  .details svg { width: 13px; height: 13px; margin-right: 8px; fill: var(--teal); flex: none; }

  .web-line {
    position: absolute; left: 0; top: 288px; width: 600px; text-align: center;
    color: var(--white); font-size: 14px; letter-spacing: 3.6px;
  }
  .service-area {
    position: absolute; left: 0; top: 312px; width: 600px; text-align: center;
    color: var(--white); font-size: 9px; font-weight: 500; letter-spacing: 3px;
  }
</style>
</head>
<body>
<div class="stage">

  <section class="card card--front">
    <div class="ornament ornament--faint-symbol" role="img" aria-label="Faint large brand symbol decoration"></div>
    <div class="ornament ornament--faint-swirl" role="img" aria-label="Faint floral swirl ornament"></div>

    <span class="brand-dot"></span>
    <div class="ornament ornament--crest" role="img" aria-label="Floral scroll ornament"></div>
    <div class="brand">
      <span class="brand__name">VELVET BLOOM</span>
      <span class="brand__tagline">MARISOL'S CLEANING SERVICE</span>
    </div>

    <span class="marker marker--one"></span>
    <span class="marker marker--two"></span>
    <div class="person">
      <div class="person__name">MARISOL DENHART</div>
      <div class="person__role">DIRECTOR</div>
    </div>

    <ul class="details">
      <li class="details__abn">ABN: 47193062857</li>
      <li>
        <svg viewBox="0 0 24 24" aria-hidden="true"><path d="M6.6 10.8c1.4 2.8 3.8 5.1 6.6 6.6l2.2-2.2c.3-.3.7-.4 1-.2 1.1.4 2.3.6 3.6.6.6 0 1 .4 1 1V20c0 .6-.4 1-1 1C10.6 21 3 13.4 3 4c0-.6.4-1 1-1h3.5c.6 0 1 .4 1 1 0 1.3.2 2.5.6 3.6.1.3 0 .7-.2 1z"/></svg>
        0418926547
      </li>
      <li>
        <svg viewBox="0 0 24 24" aria-hidden="true"><path d="M2 5h20v14H2z M2 5l10 7 10-7" stroke="#2e323f" stroke-width="1.6"/></svg>
        marisolsvelvetcleaning@brightmail.example
      </li>
      <li>
        <svg viewBox="0 0 24 24" aria-hidden="true"><circle cx="12" cy="12" r="10"/><path d="M7 8c2 0 3 1 3 3s-2 2-2 4M15 5c-1 2 0 3 2 3s3 2 2 4M13 19c0-2 1-3 3-3" stroke="#2e323f" stroke-width="1.6" fill="none"/></svg>
        www.velvetbloom.example
      </li>
    </ul>
  </section>

  <section class="card card--back">
    <span class="brand-dot"></span>
    <div class="brand">
      <span class="brand__name">VELVET BLOOM</span>
      <span class="brand__tagline">MARISOL'S CLEANING SERVICE</span>
    </div>
    <div class="ornament ornament--crest" role="img" aria-label="Floral scroll ornament"></div>
    <div class="web-line">www.velvetbloom.example</div>
    <div class="service-area">AVAILABLE SYDNEY WIDE</div>
  </section>

</div>
</body>
</html>
```